New Architectural Firm Business Cards

New Business card to compliment previous pixel forum logo (attached). Please design a business card that is simple, modern, creative....please do not use "symbols", simply the logo and associated graphics/text. The front should contain name/address/phone/email/web address (with graphics).....back should be 100% graphic design using the logo somehow. Hoping for a two color (black and yellow) design. full bleed design, no borders

Target Market(s)

Commercial Architecture Clients

Industry/Entity Type

Architecture

Contact Information for Business Card

Please design a business card that is simple, modern, creative....please do not use "symbols", simply the logo and associated graphics/text. The front should contain name/address/phone/email/web address (with graphics).....back should be 100% graphic design using the logo somehow

Font styles to use
Sans Serif

Colors
FFF300
FFF600
FEFA6F
FFFEC7
FFFEE8

Requirements
Must have
• Clean, Modern Design
Should not have
• Stock images or "icons"

```html
<!DOCTYPE html>
<html lang="en">
<head>
<meta charset="utf-8">
<title>Halden Architecture – Business Card</title>
<link href="https://fonts.googleapis.com/css2?family=Open+Sans:wght@400;700&display=swap" rel="stylesheet">
<style>
  :root{
    --backdrop:#3a3a3a;
    --card:#141414;
    --yellow:#f5c518;
    --white:#f2f2f2;
    --muted:#d8d8d8;
    --deep-mark:#262626;
  }
  *{box-sizing:border-box;margin:0;padding:0}
  html,body{width:1200px;height:801px;overflow:hidden}
  body{
    background:var(--backdrop);
    font-family:"Open Sans",Arial,sans-serif;
    position:relative;
  }
  .card{
    position:absolute;
    width:500px;height:286px;
    background:var(--card);
    border:1.5px solid var(--yellow);
  }
  .card--front{left:80px;top:130px}
  .card--back{left:620px;top:385px}

  .brand{
    position:absolute;right:34px;top:38px;
    display:flex;align-items:center;gap:10px;
    color:var(--yellow);font-weight:700;font-size:20px;letter-spacing:.5px;
  }
  .brand__square{width:14px;height:14px;background:var(--yellow)}

  .rule{position:absolute;height:1px;background:var(--yellow)}
  .rule--main{left:150px;right:34px;top:110px}
  .rule--short{left:30px;width:190px;top:196px}

  .person{position:absolute;left:30px;top:146px}
  .person__name{color:var(--yellow);font-weight:700;font-size:19px;letter-spacing:.5px;text-transform:uppercase}
  .person__role{color:var(--muted);font-size:13px;margin-top:1px}

  .contacts{position:absolute;left:30px;top:208px;list-style:none}
  .contacts li{display:flex;align-items:center;gap:8px;color:var(--white);font-size:13px;line-height:20px}
  .contacts svg{width:11px;height:11px;fill:var(--yellow)}

  .address{
    position:absolute;right:34px;top:150px;text-align:right;
    color:var(--white);font-size:13px;line-height:19px;
  }

  .back-mark{
    position:absolute;left:0;right:0;top:50%;transform:translateY(-50%);
    text-align:center;color:var(--deep-mark);font-weight:700;font-size:54px;
  }
</style>
</head>
<body>
  <section class="card card--front">
    <div class="brand"><span class="brand__square"></span>Halden Architecture</div>
    <div class="rule rule--main"></div>

    <div class="person">
      <p class="person__name">Daniel Reyes</p>
      <p class="person__role">President</p>
    </div>
    <div class="rule rule--short"></div>

    <ul class="contacts">
      <li><svg viewBox="0 0 12 12"><path d="M2.5 1 4.5 3 3.6 4.5C4.3 6 5.8 7.6 7.5 8.4L9 7.5 11 9.5 9.8 11C5.5 10.5 1.5 6.5 1 2.2Z"/></svg>555-010-4821</li>
      <li><svg viewBox="0 0 12 12"><path d="M0 2h12v1L6 7 0 3ZM0 4.3 6 8.3 12 4.3V10H0Z"/></svg>info@haldenarch.com</li>
      <li><svg viewBox="0 0 12 12"><circle cx="6" cy="6" r="5.5"/><path d="M6 .5v11M.5 6h11" stroke="#141414" stroke-width="1"/></svg>www.haldenarch.com</li>
    </ul>

    <address class="address" style="font-style:normal">
      1180 Harbor Crest Way<br>Seaview Bay CA 90000
    </address>
  </section>

  <section class="card card--back">
    <p class="back-mark">Halden</p>
  </section>
</body>
</html>
```